Web Design for ROLV Air conditioning company

Hello,

I am calling on you for the modernization of the company's website
https://clarovent-services-techniques.fr/

The new one must include the new logo with the new graphic charter (color, style ...)

I'm looking for a simple design (less is more), a font written without Serif, the logo that brings a touch of color and modernity.

(maintenance and installation company for air conditioning and ventilation systems)
COLORS: in line with the logo

CHAPTER:

# PRESENTATION
# SERVICES
AIR CONDITIONING (ice cube icon)
HEATING (flame icon)
AIR TREATMENT (icon fan)
# ACHIEVEMENTS

# CONTACT
CONTACT FORM
GOOGLE MAPS

Target Market(s)

Showcase site for our customers

Coding

Coded - Design and coding required

Number of Pages Required

4 page

Font styles to use
Sans Serif

Colors
33b8a4
33a6d7
3176b5
ffffff

Requirements
Must have
• Clear and fluid navigation
a visual identity of the page with the logo
Should not have
• Overloaded.

```html
<!DOCTYPE html>
<html lang="en">
<head>
<meta charset="utf-8">
<title>ROLV – Clarovent Technical Services</title>
<link href="https://fonts.googleapis.com/css2?family=Mulish:ital,wght@0,400;0,600;0,700;0,800;1,400;1,800&display=swap" rel="stylesheet">
<style>
:root{
  --teal:#33b8a4;
  --sky:#33a6d7;
  --blue:#3176b5;
  --white:#ffffff;
  --ink:#1f2a30;
  --grey:#6b6f73;
  --field:#c9c9c9;
  --gold:#f3c623;
}
*{box-sizing:border-box;margin:0;padding:0}
html,body{width:1200px;height:3750px;overflow:hidden;background:var(--white)}
body{position:relative;font-family:'Mulish',Arial,sans-serif;color:var(--ink)}
.abs{position:absolute}
.center{text-align:center}
.h2{font-size:31px;font-weight:800;color:var(--ink);letter-spacing:.2px}

/* header */
.header{top:0;left:0;width:1200px;height:105px;background:var(--white);border-bottom:1px solid #e3e3e3}
.brand{left:150px;top:28px;display:flex;align-items:center;gap:16px}
.brand-name{font-size:50px;font-weight:800;color:var(--ink);letter-spacing:1px;line-height:1}
.brand-tag{font-size:16px;font-weight:600;color:var(--grey);margin-top:12px}
.nav{top:68px;left:650px;font-size:12.5px;font-weight:700}
.nav a{color:var(--ink);text-decoration:none;position:absolute;white-space:nowrap}
.nav .active{color:var(--teal)}
.nav .underline{position:absolute;left:83px;top:30px;width:60px;height:2px;background:var(--teal)}

/* hero */
.hero-bg{top:105px;left:0;width:1200px;height:580px}
.hero-title{left:563px;top:212px;font-size:43px;line-height:50px;font-weight:800;font-style:italic;color:var(--white);white-space:nowrap}
.hero-sub{left:566px;top:344px;font-size:18px;font-style:italic;color:#15202a}
.btn-outline{left:563px;top:390px;width:170px;height:48px;border:2px solid var(--white);border-radius:10px 10px 10px 0;color:var(--white);font-size:13px;font-weight:600;display:flex;align-items:center;justify-content:center}
.info{top:600px;color:var(--white);font-size:12px;display:flex;align-items:center;gap:18px}
.info .ic{width:30px;height:30px;background:var(--blue);display:flex;align-items:center;justify-content:center;border-radius:3px}

/* services */
.service{top:845px;width:260px;text-align:center}
.service .frame{display:block;margin:0 auto;width:115px;height:116px}
.service h3{margin-top:18px;font-size:19px;font-weight:800;color:var(--sky)}
.service p{margin:6px auto 0;width:180px;font-size:10.5px;line-height:12.5px;color:var(--ink)}
.btn-read{display:flex;align-items:center;justify-content:center;gap:10px;margin:28px auto 0;width:135px;height:36px;background:#5e8fe6;color:var(--white);font-size:12px;font-weight:700;border-radius:10px 10px 0 10px}
.svc-ventilation h3{color:var(--teal)}
.svc-aircon h3{color:var(--blue)}

/* who */
.who-band{top:1268px;left:0;width:1200px;height:402px;background:linear-gradient(90deg,#5ab58a 0%,#33b0a0 40%,#3196c0 100%)}
.who-photo{top:1225px;left:118px;width:477px;height:353px;background:var(--white)}
.who-title{left:690px;top:1305px;font-size:30px;font-weight:800;color:#1d2a2e}
.who-sub{left:688px;top:1362px;font-size:18px;font-weight:700;color:var(--white)}
.box{border:2px solid var(--white);color:#173038;font-size:13px;line-height:15px;text-align:center;display:flex;align-items:center;justify-content:center}

/* testimonials */
.name{top:2160px;left:0;width:1200px;font-size:23px;font-weight:700;color:var(--blue)}
.quote{top:2238px;left:492px;width:253px;height:62px;border:1.5px solid #cfcfcf;border-radius:8px;font-size:10.5px;line-height:12.5px;padding:10px 8px;text-align:center}

/* achievements */
.ach-text{top:2598px;left:180px;width:840px;font-size:13px;line-height:16px;text-align:center}

/* contact */
.field{background:var(--field);border:2px solid #e6e6e6;border-radius:5px;font-size:14px;color:#2a2a2a;padding:14px 14px}
.submit{top:3228px;left:150px;width:130px;height:38px;background:var(--teal);color:var(--white);font-size:15px;font-weight:800;border-radius:4px;display:flex;align-items:center;justify-content:center}

/* footer */
.foot-col{left:790px;color:var(--white);font-size:13px}
.foot-col .small{font-size:10.5px}
.copy{top:3726px;left:0;width:1200px;text-align:center;font-size:12px;color:var(--white)}
</style>
</head>
<body>

<header class="header abs">
  <div class="brand abs">
    <span class="brand-name">ROLV</span>
    <span class="brand-tag">CLAROVENT SERVICES TECHNIQUES</span>
  </div>
  <nav class="nav abs">
    <a class="active" style="left:0">Home</a>
    <a style="left:73px">Who Are We ?</a>
    <a style="left:195px">Our Services</a>
    <a class="active" style="left:308px;color:var(--blue)">&#9742; Contact Us</a>
    <span class="underline"></span>
  </nav>
</header>

<svg class="abs hero-bg" viewBox="0 105 1200 580" width="1200" height="580" style="top:105px;left:0">
  <defs>
    <linearGradient id="heroPhoto" x1="0" x2="1">
      <stop offset="0" stop-color="#3d76b8"/><stop offset="1" stop-color="#4f8ccc"/>
    </linearGradient>
  </defs>
  <polygon points="0,105 1200,105 1200,455 1045,650 155,650 0,455" fill="#3a71b3"/>
  <polygon points="495,105 1200,105 1200,455 1045,650 495,650" fill="url(#heroPhoto)" role="img" aria-label="Photo of a technician servicing an air conditioning unit, tinted blue"/>
  <rect x="80" y="170" width="400" height="310" fill="#4a80c0" role="img" aria-label="Illustration of two technicians installing an indoor and outdoor air conditioning unit"/>
  <polygon points="120,584 1045,584 1045,650 178,650" fill="var(--teal)"/>
  <polygon points="575,650 625,650 600,676" fill="var(--teal)"/>
  <circle cx="600" cy="657" r="8" fill="none" stroke="#173038" stroke-width="3"/>
  <circle cx="600" cy="657" r="3" fill="#173038"/>
</svg>
<div class="hero-title abs">CLAROVENT TECHNICAL<br>SERVICES LYON</div>
<div class="hero-sub abs">THE SOLUTION TO YOUR MAINTENANCE PROBLEM</div>
<div class="btn-outline abs">Schedule an Appoitment</div>

<div class="info abs" style="left:180px">
  <span class="ic"><svg width="16" height="16" viewBox="0 0 24 24"><path fill="#fff" d="M6.6 10.8a15 15 0 006.6 6.6l2.2-2.2c.3-.3.7-.4 1-.2 1.1.4 2.3.6 3.6.6.6 0 1 .4 1 1V20c0 .6-.4 1-1 1A17 17 0 013 4c0-.6.4-1 1-1h3.5c.6 0 1 .4 1 1 0 1.3.2 2.5.6 3.6.1.3 0 .7-.2 1z"/></svg></span>
  <span>04 70 00 12 34</span>
</div>
<div class="info abs" style="left:462px">
  <span class="ic"><svg width="16" height="12" viewBox="0 0 16 12"><rect width="16" height="12" rx="1" fill="#fff"/><path d="M1 1l7 5 7-5" stroke="#3176b5" stroke-width="1.5" fill="none"/></svg></span>
  <span>contact@clarovent-mail.fr</span>
</div>
<div class="info abs" style="left:815px;top:598px">
  <span class="ic"><svg width="14" height="18" viewBox="0 0 14 18"><path fill="#fff" d="M7 0a7 7 0 00-7 7c0 5 7 11 7 11s7-6 7-11a7 7 0 00-7-7zm0 10a3 3 0 110-6 3 3 0 010 6z"/></svg></span>
  <span style="line-height:14px">14 Rue des Tilleuls<br>38100 VALMONT</span>
</div>

<div class="h2 abs center" style="top:768px;left:0;width:1200px">OUR SERVICES</div>

<div class="service svc-heater abs" style="left:110px">
  <svg class="frame" viewBox="0 0 115 116"><path d="M6 100V4h103v96H70M45 100H6" fill="none" stroke="var(--blue)" stroke-width="4"/><rect x="43" y="20" width="30" height="50" rx="3" fill="none" stroke="var(--teal)" stroke-width="2.5"/><path d="M58 30c4 5 5 9 0 12-5-3-3-7 0-12z" fill="none" stroke="var(--blue)" stroke-width="2"/><circle cx="58" cy="55" r="4" fill="none" stroke="var(--blue)" stroke-width="2"/><text x="58" y="108" text-anchor="middle" font-family="Mulish,sans-serif" font-weight="800" font-size="18" fill="var(--blue)">1</text></svg>
  <h3>HEATER</h3>
  <p>Lorem ipsum dolor sit amet, consec-tetur adipiscing elit, sed do eiusmod tempor incididunt ut labore et dolore magna aliqua...</p>
  <div class="btn-read">Read More <svg width="26" height="8"><path d="M0 4h24M20 1l4 3-4 3" stroke="#fff" fill="none" stroke-width="1.4"/></svg></div>
</div>
<div class="service svc-ventilation abs" style="left:470px">
  <svg class="frame" viewBox="0 0 115 116"><path d="M6 100V4h103v96H70M45 100H6" fill="none" stroke="var(--teal)" stroke-width="4"/><circle cx="58" cy="40" r="20" fill="none" stroke="var(--blue)" stroke-width="2.5"/><circle cx="58" cy="40" r="12" fill="none" stroke="var(--teal)" stroke-width="2"/><path d="M52 62h12l4 10H48z" fill="none" stroke="var(--blue)" stroke-width="2"/><text x="58" y="108" text-anchor="middle" font-family="Mulish,sans-serif" font-weight="800" font-size="18" fill="var(--blue)">2</text></svg>
  <h3>VENTILATION</h3>
  <p>Lorem ipsum dolor sit amet, consec-tetur adipiscing elit, sed do eiusmod tempor incididunt ut labore et dolore magna aliqua...</p>
  <div class="btn-read">Read More <svg width="26" height="8"><path d="M0 4h24M20 1l4 3-4 3" stroke="#fff" fill="none" stroke-width="1.4"/></svg></div>
</div>
<div class="service svc-aircon abs" style="left:827px">
  <svg class="frame" viewBox="0 0 115 116"><path d="M6 100V4h103v96H70M45 100H6" fill="none" stroke="var(--blue)" stroke-width="4"/><rect x="28" y="22" width="60" height="22" rx="3" fill="none" stroke="var(--blue)" stroke-width="2.5"/><path d="M34 36h48" stroke="var(--teal)" stroke-width="2"/><path d="M48 50v8M58 50v10M68 50v8" stroke="var(--teal)" stroke-width="2"/><circle cx="38" cy="54" r="2.5" fill="var(--teal)"/><circle cx="78" cy="54" r="2.5" fill="var(--teal)"/><text x="58" y="108" text-anchor="middle" font-family="Mulish,sans-serif" font-weight="800" font-size="18" fill="var(--blue)">3</text></svg>
  <h3>AIR CONDITIONER</h3>
  <p>Lorem ipsum dolor sit amet, consec-tetur adipiscing elit, sed do eiusmod tempor incididunt ut labore et dolore magna aliqua...</p>
  <div class="btn-read">Read More <svg width="26" height="8"><path d="M0 4h24M20 1l4 3-4 3" stroke="#fff" fill="none" stroke-width="1.4"/></svg></div>
</div>

<div class="who-band abs"></div>
<div class="who-photo abs"><div role="img" aria-label="3D figure in a hard hat holding a service wrench beside an air conditioning unit" style="margin:30px 40px;height:290px;background:linear-gradient(135deg,#f1f1f1,#d9dde0);border-radius:4px"></div></div>
<div class="who-title abs">WHO WE ARE?</div>
<div class="who-sub abs">CLAROVENT TECHNICAL SERVICES</div>
<div class="box abs" style="left:688px;top:1415px;width:116px;height:48px">Laser<br>Lineage</div>
<div class="box abs" style="left:930px;top:1415px;width:117px;height:48px">Maintenance<br>Ventilation</div>
<div class="box abs" style="left:810px;top:1472px;width:115px;height:47px">Vibration<br>Control</div>
<svg class="abs" style="left:0;top:1400px" width="1200" height="270">
  <g stroke="#111" stroke-width="3.5" fill="#111">
    <line x1="746" y1="120" x2="746" y2="80"/><polygon points="736,84 746,70 756,84" stroke="none"/>
    <line x1="868" y1="18" x2="868" y2="52"/><polygon points="858,48 868,62 878,48" stroke="none"/>
    <line x1="989" y1="120" x2="989" y2="80"/><polygon points="979,84 989,70 999,84" stroke="none"/>
  </g>
  <polygon points="560,270 640,270 600,222" fill="#fff"/>
  <circle cx="600" cy="256" r="9" fill="none" stroke="var(--blue)" stroke-width="3.5"/>
  <circle cx="600" cy="256" r="3" fill="var(--blue)"/>
</svg>

<div class="h2 abs center" style="top:1752px;left:0;width:1200px">WHAT OUR CLIENT’S ARE SAYING?</div>
<svg class="abs" style="left:0;top:1830px" width="1200" height="320">
  <circle cx="298" cy="155" r="67" fill="#3a4a5e" role="img" aria-label="Client portrait"/>
  <circle cx="600" cy="160" r="150" fill="#b7c3cf" role="img" aria-label="Portrait of the featured client"/>
  <circle cx="903" cy="155" r="67" fill="#a6a9d4" role="img" aria-label="Client portrait"/>
  <circle cx="702" cy="50" r="33" fill="var(--teal)"/>
  <path d="M702 37v26M689 50h26" stroke="#fff" stroke-width="2.5"/>
  <path d="M420 140l-22 24 22 24" stroke="var(--blue)" stroke-width="3" fill="none"/>
  <path d="M782 140l22 24-22 24" stroke="var(--blue)" stroke-width="3" fill="none"/>
</svg>
<div class="name abs center">Lucas Verner</div>
<svg class="abs" style="left:573px;top:2201px" width="92" height="18">
  <g fill="var(--gold)">
    <polygon points="8,1 10,6.5 16,7 11.5,10.5 13,16 8,13 3,16 4.5,10.5 0,7 6,6.5"/>
    <polygon transform="translate(18 0)" points="8,1 10,6.5 16,7 11.5,10.5 13,16 8,13 3,16 4.5,10.5 0,7 6,6.5"/>
    <polygon transform="translate(36 0)" points="8,1 10,6.5 16,7 11.5,10.5 13,16 8,13 3,16 4.5,10.5 0,7 6,6.5"/>
    <polygon transform="translate(54 0)" points="8,1 10,6.5 16,7 11.5,10.5 13,16 8,13 3,16 4.5,10.5 0,7 6,6.5"/>
    <polygon transform="translate(72 0)" points="8,1 10,6.5 16,7 11.5,10.5 13,16 8,13 3,16 4.5,10.5 0,7 6,6.5"/>
  </g>
</svg>
<div class="quote abs">Lorem ipsum dolor sit amet, consectetur adipisc-ing elit, sed do eiusmod tempor incididunt ut labore et dolore magna aliqua...</div>
<svg class="abs" style="left:690px;top:2228px" width="60" height="100">
  <text x="3" y="22" font-family="Mulish,sans-serif" font-weight="800" font-size="30" fill="var(--blue)">”</text>
  <path d="M50 72c-4 12-12 20-22 26 6-8 8-16 8-26" fill="#fff" stroke="#cfcfcf" stroke-width="1.5"/>
</svg>

<div class="h2 abs center" style="top:2408px;left:0;width:1200px">OUR ACHIEVEMENTS</div>
<svg class="abs" style="left:0;top:2490px" width="1200" height="200">
  <g fill="var(--teal)">
    <rect x="189" y="18" width="67" height="38" rx="14"/>
    <rect x="350" y="10" width="90" height="54" rx="16"/>
    <rect x="535" y="2" width="134" height="72" rx="18"/>
    <rect x="764" y="10" width="89" height="54" rx="16"/>
    <rect x="947" y="18" width="68" height="38" rx="14"/>
  </g>
  <g fill="#5d6a70">
    <circle cx="222" cy="37" r="11"/>
    <circle cx="395" cy="37" r="19"/>
    <circle cx="602" cy="38" r="30"/>
    <circle cx="808" cy="37" r="19"/>
    <circle cx="981" cy="37" r="11"/>
  </g>
  <polygon points="566,170 575,175 575,185 566,190 557,185 557,175" fill="#999"/>
  <polygon points="599,170 608,175 608,185 599,190 590,185 590,175" fill="var(--blue)"/>
  <polygon points="632,170 641,175 641,185 632,190 623,185 623,175" fill="#999"/>
</svg>
<div class="ach-text abs">Lorem ipsum dolor sit amet, consectetur adipiscing elit, sed do eiusmod tempor incididunt ut labore et dolore magna aliqua. Ut enim ad minim veniam, quis nostrud exercitation ullamco laboris nisi ut aliquip ex ea commodo consequat.</div>

<div class="abs" style="top:2790px;left:0;width:700px;height:480px;background:linear-gradient(90deg,rgba(230,230,230,.0),rgba(235,235,235,.45),rgba(230,230,230,0))" role="img" aria-label="Faint background of hand tools"></div>
<div class="h2 abs" style="top:2860px;left:150px">CONTACT US</div>
<div class="abs" style="top:2900px;left:152px;font-size:16.5px;line-height:26px;color:var(--teal)">We react promptly to your service needs,<br>don’t hesitate to call.</div>
<div class="field abs" style="top:2975px;left:150px;width:265px;height:47px">Your Name</div>
<div class="field abs" style="top:2975px;left:443px;width:265px;height:47px">Phone Number</div>
<div class="field abs" style="top:3035px;left:150px;width:265px;height:47px">Email Address</div>
<div class="field abs" style="top:3035px;left:443px;width:265px;height:47px">Select a Service
  <svg class="abs" style="right:8px;top:16px" width="14" height="11"><polygon points="0,0 14,0 7,11" fill="#fff"/></svg></div>
<div class="field abs" style="top:3095px;left:150px;width:558px;height:100px">Message</div>
<div class="submit abs">SUBMIT</div>
<div class="abs" style="top:2765px;left:730px;width:400px;height:520px;background:linear-gradient(180deg,#f0a64a 0%,#d9e84a 40%,#c6d64e 75%,#5e6f86 100%);border-radius:40px 40px 0 0;opacity:.85" role="img" aria-label="Smiling worker in a hard hat and high-visibility vest pointing toward the form"></div>

<svg class="abs" style="left:0;top:3370px" width="1200" height="380">
  <polygon points="178,4 575,4 600,32 625,4 1030,4 1200,134 1200,380 0,380 0,134" fill="#3a7fc5"/>
  <circle cx="600" cy="13" r="8" fill="none" stroke="var(--teal)" stroke-width="3.5"/>
  <circle cx="600" cy="13" r="2.5" fill="var(--teal)"/>
  <polygon points="365,50 525,50 590,185 525,320 365,320 300,185" fill="#dfe4e6" role="img" aria-label="Map showing the company location"/>
  <circle cx="447" cy="192" r="7" fill="#d83a3a"/>
  <line x1="585" y1="152" x2="770" y2="60" stroke="#fff" stroke-width="1"/>
  <circle cx="772" cy="60" r="6" fill="#fff"/><circle cx="772" cy="60" r="3" fill="#d83a3a"/>
  <circle cx="806" cy="188" r="14" fill="#fff"/>
  <circle cx="851" cy="188" r="14" fill="#fff"/>
  <circle cx="896" cy="188" r="14" fill="#fff"/>
  <path d="M792 262c2 4 5 7 9 9l2-2c1 0 2 0 3 .5v3c0 .5-.5 1-1 1-6 0-13-7-13-13 0-.5.5-1 1-1h3c.5 1 .5 2 0 3z" fill="#fff"/>
  <rect x="790" y="290" width="15" height="11" fill="#fff"/><path d="M790 290l7.5 6 7.5-6" stroke="#3a7fc5" fill="none"/>
</svg>
<div class="abs" style="top:3628px;left:183px;font-size:50px;font-weight:800;color:var(--white);letter-spacing:1px">ROLV</div>
<div class="foot-col abs" style="top:3425px">Address</div>
<div class="foot-col abs small" style="top:3450px">14 Rue des Tilleuls</div>
<div class="foot-col abs small" style="top:3477px">38100 VALMONT</div>
<div class="foot-col abs" style="top:3515px">Keep Connected</div>
<div class="foot-col abs" style="top:3603px">OUR CONTACT</div>
<div class="foot-col abs small" style="left:816px;top:3628px">+1 555-010-2040</div>
<div class="foot-col abs small" style="left:816px;top:3655px">info@clarovent-mail.com</div>
<div class="copy abs">@ 2016 Clarovent Technical Services | Privacy Policy | Sitemap</div>

</body>
</html>
```